Design business cards for Ironvale Barbers (Opening March so won't need finalised till January2018

Ironvale Barbers is the new age barbers and skincare for all men. Creating tailor made haircuts & customised skincare solutions for the perfect healthy manly look. The Barbers will have a industrial, rustic, worldly feel about it. Rustic red brick wall with old wine barrels as the work stations with the old fashion barber chairs. Concrete floor and a bit corrugated iron around.
Target Market(s)
Professional males who like a great haircut, wet shave and may consider a facial if in the right environment. Total pampering experience in a boys environment.
Industry/Entity Type
Barber
Contact Information for Business Card
Front- Logo - address is 42 Kowhai Rd Taupo
Ph - (07) 348 6192
www.ironvalebarbers.com
email - hello@ironvale.co.nz
Back of card
Mens Haircare - Wet Shaving - Facials - Skin Prescriptions
We are doing a loyalty program - 6 squares numbered then 7th free
Colors
Designer to choose colors to be used in the design.
Requirements
Must have
- Clean simple easy to read.
Nice to have
- Our current colours are white font on black background but thinking we need to introduce another colour. Maybe white logo on a copper, bronze or rusty background. Or even a rustic red brick wall with white writing. Want it clean simple to read. Maybe a burgundy?
Should not have
- no images like heads, scissors, razors please

```html
<!DOCTYPE html>
<html lang="en">
<head>
<meta charset="utf-8">
<title>Ironvale Barbers – Business Cards</title>
<link href="https://fonts.googleapis.com/css2?family=Montserrat:wght@500;600&family=Dancing+Script:wght@500&display=swap" rel="stylesheet">
<style>
  :root {
    --page: #e6e6e4;
    --gold: #c9962e;
    --gold-light: #e8c15a;
    --ink: #111111;
    --white: #ffffff;
    --brown-dark: #2a1e14;
    --brown-mid: #5a4330;
    --brick: #8a4a36;
    --stone: #9a938a;
    --band: rgba(255,255,255,0.82);
  }
  * { margin: 0; padding: 0; box-sizing: border-box; }
  html, body { width: 1200px; height: 900px; overflow: hidden; background: var(--page); }
  .canvas { position: relative; width: 1200px; height: 900px; }
  .card {
    position: absolute; left: 320px; width: 560px; height: 320px;
    overflow: hidden; box-shadow: 0 10px 24px rgba(0,0,0,0.35);
  }
  .card--front { top: 100px; }
  .card--back { top: 480px; }

  /* Front */
  .front-photo {
    position: absolute; inset: 0;
    background: radial-gradient(circle at 75% 35%, #7a5a3a 0%, var(--brown-mid) 35%, var(--brown-dark) 80%);
  }
  .front-lens { position: absolute; inset: 0; }
  .brand {
    position: absolute; left: 60px; width: 360px; top: 78px; text-align: center;
    font-family: "Montserrat", sans-serif; font-weight: 600; color: var(--gold-light);
  }
  .brand__name { font-size: 44px; letter-spacing: 2px; line-height: 1; }
  .brand__sub { font-size: 16px; letter-spacing: 8px; margin-top: 6px; }
  .contact {
    position: absolute; left: 168px; top: 178px; list-style: none;
    font-family: "Montserrat", sans-serif; font-weight: 500; font-size: 14px;
    color: var(--gold-light); letter-spacing: 0.6px;
  }
  .contact li { display: flex; align-items: center; height: 26px; }
  .contact svg { width: 18px; height: 18px; margin-right: 10px; flex: none; }

  /* Back */
  .back-photo {
    position: absolute; inset: 0;
    background: linear-gradient(180deg, var(--stone) 0%, var(--brick) 45%, #4b3a32 80%, #2b2624 100%);
  }
  .service-band {
    position: absolute; left: 0; top: 128px; width: 400px; height: 118px;
    background: var(--band);
  }
  .services {
    position: absolute; left: 14px; top: 137px; white-space: nowrap;
    font-family: "Dancing Script", cursive; font-size: 14px; color: var(--ink);
  }
  .field {
    position: absolute; left: 30px; display: flex; align-items: flex-end;
    font-family: "Dancing Script", cursive; font-size: 19px; color: var(--ink);
  }
  .field__line { width: 240px; border-bottom: 1px solid var(--ink); margin-left: 8px; height: 18px; }
  .field--date { top: 170px; }
  .field--time { top: 206px; }
  .back-brand {
    position: absolute; left: 120px; width: 240px; top: 258px; text-align: center;
    font-family: "Montserrat", sans-serif; font-weight: 600; color: var(--white);
  }
  .back-brand__name { font-size: 26px; letter-spacing: 1px; line-height: 1; }
  .back-brand__sub { font-size: 10px; letter-spacing: 6px; margin-top: 3px; }
  .welcome-panel { position: absolute; inset: 0; }
</style>
</head>
<body>
<main class="canvas">

  <section class="card card--front" aria-label="Business card front">
    <div class="front-photo" role="img" aria-label="Photo of barber shop interior with chair and grooming tools"></div>
    <svg class="front-lens" viewBox="0 0 560 320" aria-hidden="true">
      <circle cx="240" cy="160" r="190" fill="rgba(10,10,12,0.6)"/>
      <circle cx="240" cy="160" r="190" fill="none" stroke="var(--gold)" stroke-width="7"/>
      <line x1="92" y1="148" x2="150" y2="144" stroke="var(--gold)" stroke-width="2"/>
      <line x1="330" y1="144" x2="388" y2="148" stroke="var(--gold)" stroke-width="2"/>
    </svg>
    <div class="brand">
      <div class="brand__name">IRONVALE</div>
      <div class="brand__sub">BARBERS</div>
    </div>
    <ul class="contact">
      <li>
        <svg viewBox="0 0 20 20"><circle cx="10" cy="10" r="10" fill="var(--gold)"/><path d="M10 4.5a3.5 3.5 0 0 0-3.5 3.5c0 2.6 3.5 7 3.5 7s3.5-4.4 3.5-7A3.5 3.5 0 0 0 10 4.5zm0 5a1.4 1.4 0 1 1 0-2.8 1.4 1.4 0 0 1 0 2.8z" fill="var(--ink)"/></svg>
        42 Kowhai Rd Taupo
      </li>
      <li>
        <svg viewBox="0 0 20 20"><circle cx="10" cy="10" r="10" fill="var(--gold)"/><path d="M6.5 5h2l1 2.5-1.3 1a6 6 0 0 0 3.3 3.3l1-1.3 2.5 1v2a1 1 0 0 1-1 1A8.5 8.5 0 0 1 5.5 6a1 1 0 0 1 1-1z" fill="var(--ink)"/></svg>
        (07) 348 6192
      </li>
      <li>
        <svg viewBox="0 0 20 20"><circle cx="10" cy="10" r="10" fill="var(--gold)"/><circle cx="10" cy="10" r="5" fill="none" stroke="var(--ink)" stroke-width="1.2"/><path d="M5 10h10M10 5c-2 2.6-2 7.4 0 10M10 5c2 2.6 2 7.4 0 10" fill="none" stroke="var(--ink)" stroke-width="1.1"/></svg>
        www.ironvalebarbers.com
      </li>
      <li>
        <svg viewBox="0 0 20 20"><circle cx="10" cy="10" r="10" fill="var(--gold)"/><rect x="5" y="6.5" width="10" height="7" fill="none" stroke="var(--ink)" stroke-width="1.2"/><path d="M5 6.5l5 4 5-4" fill="none" stroke="var(--ink)" stroke-width="1.2"/></svg>
        hello@ironvale.co.nz
      </li>
    </ul>
  </section>

  <section class="card card--back" aria-label="Business card back">
    <div class="back-photo" role="img" aria-label="Photo of barber shop with red brick wall, windows and barber chairs"></div>
    <div class="service-band"></div>
    <p class="services">Mens Haircare - Wet Shaving - Facials - Skin Prescriptions</p>
    <div class="field field--date">Date -<span class="field__line"></span></div>
    <div class="field field--time">Time -<span class="field__line"></span></div>
    <div class="back-brand">
      <div class="back-brand__name">IRONVALE</div>
      <div class="back-brand__sub">BARBERS</div>
    </div>
    <svg class="welcome-panel" viewBox="0 0 560 320">
      <path d="M400 0 C 340 90, 340 230, 400 320 L560 320 L560 0 Z" fill="var(--ink)"/>
      <path d="M400 0 C 340 90, 340 230, 400 320" fill="none" stroke="var(--gold)" stroke-width="6"/>
      <rect x="390" y="20" width="150" height="280" fill="#1c1c1c" role="img" aria-label="Hand-lettered chalk sign reading Welcome to the Man Salon with shaving brush and flourishes"/>
    </svg>
  </section>

</main>
</body>
</html>
```